Tailbrook Website Design

Need a website for a Dog Grooiming business. Please make it simular to these:

https://www.furvanto.com
https://haulnorix.com
https://meadowpetrin.com
https://www.drivelumo.com/search/

```html
<!DOCTYPE html>
<html lang="en">
<head>
<meta charset="utf-8">
<title>Tailbrook – Dog Grooming</title>
<link href="https://fonts.googleapis.com/css2?family=Exo+2:wght@600;700;800&family=Poppins:wght@400;500;600&display=swap" rel="stylesheet">
<style>
:root{
  --teal:#129b96;
  --teal-deep:#0b8c88;
  --orange:#f7941d;
  --cream:#fff3e6;
  --ink:#1f2326;
  --muted:#6b6f73;
  --navy:#0b4a66;
  --footer:#2b2722;
  --white:#ffffff;
}
*{box-sizing:border-box;margin:0;padding:0}
html,body{width:1200px;height:4243px;overflow:hidden;background:var(--white)}
body{position:relative;font-family:"Poppins",sans-serif;color:var(--ink)}
.abs{position:absolute}
.head{font-family:"Exo 2",sans-serif;font-weight:700}
.rule{display:inline-block;width:36px;height:2px;background:var(--orange);vertical-align:middle;margin-left:12px}

/* nav */
.brand{left:59px;top:8px;font-family:"Poppins",sans-serif;font-weight:600;font-size:26px;color:var(--ink)}
.nav{top:24px;left:585px;display:flex;gap:33px;font-size:13px}
.nav a{color:var(--ink);text-decoration:none}
.nav a.active{color:var(--orange)}
.quote-btn{left:1015px;top:16px;width:122px;height:36px;border-radius:18px;background:var(--teal);color:#fff;font-size:13px;font-weight:600;display:flex;align-items:center;justify-content:center}

/* hero */
.hero-title1{left:61px;top:215px;font-size:64px;color:var(--orange);font-weight:800;letter-spacing:1px}
.hero-title2{left:61px;top:295px;font-size:66px;color:#fff;font-weight:800;letter-spacing:1px}
.hero-text{left:61px;top:384px;width:430px;font-size:12px;line-height:20px;color:#fff}
.btn-orange{left:61px;top:458px;width:155px;height:35px;border-radius:18px;background:var(--orange);color:#fff;font-size:13px;font-weight:600;display:flex;align-items:center;justify-content:center}

/* services */
.section-title{font-size:32px;color:var(--teal)}
.services-title{left:0;width:1200px;top:685px;text-align:center}
.services-title .rule{margin:0 10px}
.card{top:758px;width:285px;height:432px;background:#fff;box-shadow:0 4px 14px rgba(0,0,0,.06);border-radius:4px}
.card-top{left:0;top:0;width:285px;height:198px;background:#fde6d2;border-radius:4px 4px 0 0}
.card.featured .card-top{background:var(--teal)}
.card-photo{left:62px;top:102px;width:160px;height:160px;border-radius:50%;border:6px solid #fff;background:linear-gradient(135deg,#c9b39a,#7a6a5c)}
.card.featured .card-photo{border-radius:22px;background:linear-gradient(135deg,#e2c79a,#9c8a6f)}
.card h3{position:absolute;top:278px;width:100%;text-align:center;font-size:15px;font-weight:600}
.card p{position:absolute;top:306px;left:22px;width:241px;text-align:center;font-size:12px;line-height:20px;color:var(--muted)}
.card-arrow{left:112px;top:400px;width:60px;height:60px;border-radius:50%;background:#fdeee0;display:flex;align-items:center;justify-content:center}
.card.featured .card-arrow{background:#e4f3f2}

/* signature */
.sig-title{left:165px;top:1420px;font-size:38px;line-height:46px;color:var(--teal)}
.sig-text{left:165px;top:1533px;width:340px;font-size:12px;line-height:20px;color:var(--ink)}
.call{left:165px;top:1627px;display:flex;align-items:center;gap:14px;font-size:14px;font-weight:600}
.call-ico{width:42px;height:42px;border-radius:50%;background:var(--orange);border:4px solid #fde0bf;display:flex;align-items:center;justify-content:center}
.btn-navy{top:1700px;width:90px;height:36px;border-radius:18px;background:linear-gradient(90deg,var(--navy),#0f6e8a);color:#fff;font-size:13px;font-weight:600;display:flex;align-items:center;justify-content:center}

/* video */
.video-box{left:750px;top:1895px;width:315px;height:261px;background:var(--teal-deep);border-radius:4px;color:#fff;padding:38px 28px}
.video-box h3{font-family:"Exo 2",sans-serif;font-size:28px;font-weight:700}
.video-box p{margin-top:18px;font-size:12px;line-height:20px}
.play{margin-top:22px;display:flex;align-items:center;gap:12px;font-size:14px;font-weight:600}
.play-ico{width:40px;height:40px;border-radius:50%;background:var(--orange);border:3px solid #ffd09a;display:flex;align-items:center;justify-content:center}

/* testimonials */
.testi-title{left:651px;top:2355px;font-size:38px;color:var(--teal)}
.quote-mark{left:648px;top:2426px;font-family:"Exo 2",sans-serif;font-size:60px;color:var(--orange);opacity:.8;line-height:1}
.testi-text{left:664px;top:2446px;width:385px;font-size:12px;line-height:20px;color:var(--ink)}
.stars{left:664px;top:2545px;color:var(--orange);font-size:13px;letter-spacing:2px}
.avatar{left:664px;top:2580px;width:44px;height:44px;border-radius:50%;background:linear-gradient(135deg,#b7a28c,#6f5f52)}
.client{left:740px;top:2582px;font-size:14px;line-height:24px}
.client b{color:var(--orange);font-weight:500;display:block}
.client span{color:var(--teal)}
.dots{left:663px;top:2671px;display:flex;gap:6px}
.dots i{display:block;width:30px;height:3px;background:#f3d7bc}
.dots i:first-child{background:var(--teal)}

/* partners */
.partners-title{left:0;width:1200px;top:2862px;text-align:center;font-size:40px;color:#fff}
.badge{top:2940px;width:188px;height:86px;border:2px solid rgba(255,255,255,.85);display:flex;align-items:center;justify-content:center}
.badge i{display:block;width:52px;height:52px;border-radius:50%;background:rgba(255,255,255,.85)}

/* follow */
.follow-title{left:152px;top:3226px;font-size:38px;color:var(--teal)}
.social{top:3287px;display:flex;gap:22px;left:150px}
.social i{display:block;width:14px;height:14px;border-radius:50%;background:var(--orange)}
.social i:nth-child(2){background:var(--teal);border-radius:3px}
.handle{left:150px;top:3320px;font-size:12px;color:var(--teal)}
.tile{width:217px;height:218px}

/* footer */
.foot-brand{left:59px;top:3945px;font-size:28px;font-weight:600;color:var(--orange)}
.foot-h{font-family:"Exo 2",sans-serif;font-weight:700;font-size:22px;color:var(--orange)}
.sitemap{left:432px;top:3998px;list-style:none;color:#fff;font-size:12px;line-height:24px}
.fcircles{left:803px;top:3990px;display:flex;gap:8px}
.fcircles i{display:block;width:36px;height:36px;border-radius:50%;background:var(--teal)}
.copyright{left:0;top:4207px;width:1200px;height:36px;background:var(--orange);color:#fff;font-size:12px;display:flex;align-items:center;justify-content:center}
</style>
</head>
<body>

<!-- HERO -->
<div class="abs" role="img" aria-label="Groomer brushing a golden long-haired dog" style="left:0;top:0;width:1200px;height:670px;background:linear-gradient(110deg,#e8e2da 0%,#d8b08a 45%,#b9783f 70%,#e9ddd0 100%)"></div>
<svg class="abs" style="left:0;top:0" width="1200" height="680" viewBox="0 0 1200 680" aria-hidden="true">
  <path d="M0,150 C60,95 180,82 265,95 C420,122 512,255 497,385 C482,505 400,585 300,602 L0,662 Z" fill="#129b96"/>
  <path d="M0,662 C280,618 480,588 680,592 C900,596 1090,620 1200,660 L1200,680 L0,680 Z" fill="#fff"/>
</svg>
<div class="abs" style="left:0;top:0;width:1200px;height:80px;background:linear-gradient(#fff,rgba(255,255,255,0))"></div>

<div class="abs brand">Tailbrook</div>
<nav class="abs nav">
  <a class="active">Home</a><a>Location</a><a>Careers</a><a>About Us</a><a>Blog</a><a>FAQ</a>
</nav>
<div class="abs quote-btn">FREE QUOTE</div>

<div class="abs head hero-title1">DOOR SET</div>
<div class="abs head hero-title2">DOG GROOMING</div>
<p class="abs hero-text">Contrary to popular belief, Lorem Ipsum is not simply random text. It has roots in a piece of classical Latin literature from 45 BC, making it over 2000 years old.</p>
<div class="abs btn-orange">BOOK ONLINE</div>

<!-- SERVICES -->
<div class="abs head section-title services-title"><span class="rule"></span>OUR SERVICES<span class="rule"></span></div>

<div class="abs card" style="left:142px">
  <div class="abs card-top"></div>
  <div class="abs card-photo" role="img" aria-label="Dog being washed with a shower head"></div>
  <h3>Warm Filtered Water Bath</h3>
  <p>There are many variations of passages of Lorem Ipsum available, but the majority have suffered alteration in some form</p>
  <div class="abs card-arrow"><svg width="20" height="14" viewBox="0 0 20 14"><path d="M1,7H18M12,1l6,6-6,6" stroke="#1f2326" stroke-width="1.6" fill="none"/></svg></div>
</div>
<div class="abs card featured" style="left:456px">
  <div class="abs card-top"></div>
  <div class="abs card-photo" role="img" aria-label="Small dog having its nails trimmed"></div>
  <h3>Trim &amp; File Nails</h3>
  <p>There are many variations of passages of Lorem Ipsum available, but the majority have suffered alteration in some form</p>
  <div class="abs card-arrow"><svg width="20" height="14" viewBox="0 0 20 14"><path d="M1,7H18M12,1l6,6-6,6" stroke="#1f2326" stroke-width="1.6" fill="none"/></svg></div>
</div>
<div class="abs card" style="left:771px">
  <div class="abs card-top"></div>
  <div class="abs card-photo" role="img" aria-label="Small terrier having its teeth brushed" style="background:linear-gradient(135deg,#d19a5a,#6e4a2c)"></div>
  <h3>Warm Filtered Water Bath</h3>
  <p>There are many variations of passages of Lorem Ipsum available, but the majority have suffered alteration in some form</p>
  <div class="abs card-arrow"><svg width="20" height="14" viewBox="0 0 20 14"><path d="M1,7H18M12,1l6,6-6,6" stroke="#1f2326" stroke-width="1.6" fill="none"/></svg></div>
</div>

<!-- VIDEO PHOTO (sits behind curves) -->
<div class="abs" role="img" aria-label="Groomer clipping a white poodle" style="left:0;top:1700px;width:1200px;height:570px;background:linear-gradient(100deg,#3a3340 0%,#6d6470 40%,#b9b2ae 60%,#5b5456 100%)"></div>
<svg class="abs" style="left:0;top:1300px" width="1200" height="980" viewBox="0 0 1200 980" aria-hidden="true">
  <path d="M0,100 C300,25 500,8 640,10 C850,12 1050,50 1200,95 L1200,465 C1050,515 850,545 640,546 C420,547 200,505 0,462 Z" fill="#fff3e6"/>
  <path d="M0,892 C250,950 450,966 640,966 C850,966 1050,940 1200,892 L1200,980 L0,980 Z" fill="#fff"/>
</svg>

<!-- SIGNATURE -->
<div class="abs head sig-title">Dog Grooming<br>Signature Service<span class="rule"></span></div>
<p class="abs sig-text">Lorem Ipsum is simply dummy text of the printing and typesetting industry. Lorem Ipsum has been the industry's standard dummy text ever since the 1500s, when an unknown printer took</p>
<div class="abs call">
  <div class="call-ico"><svg width="16" height="16" viewBox="0 0 24 24"><path d="M6.6,10.8a15.1,15.1,0,0,0,6.6,6.6l2.2-2.2a1,1,0,0,1,1-.25,11.4,11.4,0,0,0,3.6.57,1,1,0,0,1,1,1V20a1,1,0,0,1-1,1A17,17,0,0,1,3,4,1,1,0,0,1,4,3H7.5a1,1,0,0,1,1,1,11.4,11.4,0,0,0,.57,3.6,1,1,0,0,1-.25,1Z" fill="#1f2326"/></svg></div>
  CALL : 555 014 2276
</div>
<div class="abs btn-navy" style="left:165px">TEXT</div>
<div class="abs btn-navy" style="left:270px">CALL</div>
<div class="abs" role="img" aria-label="Yorkshire terrier with groomer's scissors and comb" style="left:808px;top:1400px;width:392px;height:363px;background:radial-gradient(ellipse at 45% 60%,#a07048 0%,#c7a080 35%,rgba(255,243,230,0) 70%)"></div>

<!-- VIDEO BOX -->
<div class="abs video-box">
  <h3>Watch &nbsp;A &nbsp;Video<span class="rule"></span></h3>
  <p>There are many variations of passages of Lorem Ipsum available, but the majority have suffered alteration in some form</p>
  <div class="play"><div class="play-ico"><svg width="14" height="14" viewBox="0 0 14 14"><path d="M3,1.5 12,7 3,12.5Z" fill="none" stroke="#fff" stroke-width="1.6"/></svg></div>PLAY VIDEO</div>
</div>

<!-- TESTIMONIALS -->
<svg class="abs" style="left:110px;top:2325px" width="400" height="400" viewBox="0 0 400 400">
  <path d="M150,10 C230,-5 250,60 300,110 C360,170 400,260 340,320 C280,385 120,390 60,340 C0,290 10,200 40,140 C70,80 90,20 150,10Z" fill="#f0f0f0"/>
  <path d="M120,55 C200,40 240,50 320,45 C380,42 400,110 380,170 C360,230 400,300 330,350 C280,390 250,400 210,390 C160,380 110,360 70,330 C30,300 40,240 50,190 C60,130 60,70 120,55Z" fill="#8a7c6e" role="img" aria-label="Woman with a husky dog"/>
</svg>
<div class="abs head testi-title">Testimonials<span class="rule"></span></div>
<div class="abs quote-mark">“</div>
<p class="abs testi-text">It is a long established fact that a reader will be distracted by the readable content of a page when looking at its layout. The point of using Lorem Ipsum is that it has a more by injected humour, or randomised words which don't look even slightly believable.</p>
<div class="abs stars">★★★★★</div>
<div class="abs avatar" role="img" aria-label="Client portrait"></div>
<div class="abs client"><b>Client Name</b><span>Dog &nbsp;Lover</span></div>
<div class="abs dots"><i></i><i></i><i></i></div>

<!-- PARTNERS -->
<svg class="abs" style="left:0;top:2740px" width="1200" height="420" viewBox="0 0 1200 420" aria-hidden="true">
  <path d="M808,40 C900,5 1050,0 1200,30 L1200,70 L808,70Z" fill="#f7941d"/>
  <path d="M0,370 C200,380 400,392 560,388 C420,412 220,420 0,408 Z" fill="#f7941d"/>
  <path d="M0,40 C250,20 500,30 700,55 C900,80 1050,50 1200,45 L1200,395 C1000,410 800,400 600,388 C400,376 200,365 0,370 Z" fill="#129b96"/>
</svg>
<div class="abs head partners-title">Partners<span class="rule"></span></div>
<div class="abs badge" style="left:84px"><i></i></div>
<div class="abs badge" style="left:294px"><i></i></div>
<div class="abs badge" style="left:503px"><i></i></div>
<div class="abs badge" style="left:714px"><i></i></div>
<div class="abs badge" style="left:923px"><i></i></div>

<!-- FOLLOW -->
<div class="abs head follow-title">Follow Us<span class="rule"></span></div>
<div class="abs social"><i></i><i></i><i></i><i></i></div>
<div class="abs handle">@ tailbrook_groom</div>

<div class="abs tile" role="img" aria-label="Woman grooming a long-haired dog" style="left:150px;top:3350px;background:linear-gradient(135deg,#c9b08e,#6e5a4a)"></div>
<div class="abs tile" role="img" aria-label="Dog being washed in a bath" style="left:150px;top:3579px;background:linear-gradient(135deg,#d8ccbf,#a3886b)"></div>
<div class="abs tile" role="img" aria-label="Groomer blow-drying a small dog" style="left:377px;top:3309px;background:linear-gradient(135deg,#e8e4e0,#a99580)"></div>
<div class="abs tile" role="img" aria-label="Corgi in a bath with foam" style="left:377px;top:3538px;background:linear-gradient(135deg,#f1efec,#c9a67e)"></div>
<div class="abs tile" role="img" aria-label="Dog having its paw clipped on grass" style="left:605px;top:3268px;background:linear-gradient(135deg,#6c8b45,#d8cbb5)"></div>
<div class="abs tile" role="img" aria-label="Schnauzer being trimmed with scissors" style="left:605px;top:3497px;background:linear-gradient(135deg,#9a9aa2,#4b4a50)"></div>
<div class="abs tile" role="img" aria-label="Groomer drying a white dog at a salon table" style="left:832px;top:3227px;background:linear-gradient(135deg,#dfe1e3,#7b7e84)"></div>
<div class="abs tile" role="img" aria-label="Woman hugging a dog outdoors" style="left:832px;top:3456px;background:linear-gradient(135deg,#7fa35a,#c49566)"></div>

<!-- FOOTER -->
<svg class="abs" style="left:0;top:3850px" width="1200" height="360" viewBox="0 0 1200 360" role="img" aria-label="Dark background photo of a groomed dog">
  <path d="M0,10 C300,30 500,35 700,28 C900,20 1050,10 1200,0 L1200,360 L0,360 Z" fill="#2b2722"/>
</svg>
<div class="abs foot-brand">Tailbrook</div>
<div class="abs foot-h" style="left:432px;top:3950px">Site Map</div>
<ul class="abs sitemap">
  <li>- Home</li><li>- About Us</li><li>- Careers</li><li>- Blog</li><li>- Terms &amp; Condition</li><li>- Privacy Policy</li><li>- FAQ</li>
</ul>
<div class="abs foot-h" style="left:803px;top:3950px">Follow Us</div>
<div class="abs fcircles"><i></i><i></i><i></i><i></i></div>
<div class="abs copyright">Copyright 2021 © Tailbrook - All Right Reserved.</div>

</body>
</html>
```